Sassy, natural personal lubricant knows that it is not always about the packaging

An opportunity exists to create packaging for the world's first Macadamia Oil personal lubricant - Worrabee Silk. Unlike any other personal lubricants, this product is created from pure macadamia nut oil. The fatty acids naturally occurring in Macadamia oil are highly anti-inflammatory and are the closest in composition to human skin lipids. Using Worrabee Silk in such a vulnerable part of our bodies is the safest and gentlest way to enhance sexual enjoyment while moisturizing and adding lubrication. Worrabee Silk is completely free of the parabens, glycerins, fragrances, hormones, silicones and petroleum products known to irritate the delicate vaginal wall.

Design tone for Worrabee Silk:
- intelligent, but not condescending or patronizing
- elegant and dignified but not prudish
- clean, natural, uninhibited

Design specs:
- See attached file for packaging specs

Colors:
- refer to www.worrabee-example.com to see other products in the range. This is a guide only. Use of those colors is not mandatory.

Ingredients:

100% Macadamia Oil

Additional features:

- edible
- vegan
- gluten-free
- low allergen
- naturally anti-microbial and anti-inflammatory

See http://thebarebotanist-example.com/benefits-of-macadamia-nut-oil-in-skin-care/ for a list of the benefits of macadamia oil.

Target Market(s)

Our target market are the early adopters within the baby boomer set. Their age is a badge of honor, they are comfortable in their own skin and as sensual and fun-loving as ever. They are in their prime - still cool, still curious, still a little crazy. They are open to new possibilities, just as they have been at every age and stage. They still have plenty to do and plenty to enjoy. Being pre-menopausal or menopausal, natural lubrication may be diminishing. Worrabee Silk is the completely natural way to bring back the pleasure in sex.

Requirements
Must have
• Brandname: Worrabee Silk

Container Packaging specs: http://www.kelvorpackware-example.com/images/art/4871K07-C-FERN-RAISED.PDF
Dispenser: http://www.kelvorpackware-example.com/lotion-dispenser-pumps/p/kQT720R/
Should not have
• No post-coital pictures
No people
Nothing phallic

```html
<!DOCTYPE html>
<html lang="en">
<head>
<meta charset="utf-8">
<title>Worrabee Silk – Lavender Scented Lubricant Label</title>
<link rel="stylesheet" href="https://fonts.googleapis.com/css2?family=Crimson+Text:wght@400;700&family=Great+Vibes&display=swap">
<style>
  :root {
    --backdrop: #e4e4e0;
    --label-white: #fbfbf8;
    --plum: #6a1f5c;
    --plum-deep: #561650;
    --lime: #a6bd2e;
    --lime-soft: rgba(166, 189, 46, 0.22);
  }
  * { box-sizing: border-box; margin: 0; padding: 0; }
  html, body {
    width: 1200px;
    height: 1000px;
    overflow: hidden;
  }
  body {
    background: var(--backdrop);
    display: flex;
    align-items: center;
    justify-content: center;
  }
  .label {
    position: relative;
    width: 440px;
    height: 820px;
    background: var(--label-white);
    overflow: hidden;
    box-shadow: 0 4px 18px rgba(0, 0, 0, 0.08);
  }
  .label__band {
    position: absolute;
    left: 0;
    width: 100%;
    height: 26px;
    background: var(--plum);
  }
  .label__band--top { top: 0; border-bottom: 4px solid var(--lime); }
  .label__band--bottom { bottom: 0; border-top: 4px solid var(--lime); }
  .label__leaf-art {
    position: absolute;
    inset: 30px 0 30px 0;
    background:
      radial-gradient(ellipse 60% 35% at 85% 25%, var(--lime-soft), transparent 70%),
      radial-gradient(ellipse 55% 40% at 35% 72%, var(--lime-soft), transparent 70%);
  }
  .label__content {
    position: relative;
    height: 100%;
    display: flex;
    flex-direction: column;
    align-items: center;
    padding-top: 70px;
    text-align: center;
    color: var(--plum);
    font-family: "Crimson Text", Georgia, serif;
  }
  .brand-mark {
    width: 150px;
    height: 150px;
    border-radius: 50%;
    border: 8px solid var(--plum);
  }
  .brand-name {
    margin-top: 34px;
    font-size: 92px;
    font-weight: 700;
    line-height: 1;
    color: var(--plum-deep);
    letter-spacing: -1px;
  }
  .product-name {
    margin-top: 14px;
    font-family: "Great Vibes", cursive;
    font-size: 86px;
    line-height: 1;
    color: var(--lime);
  }
  .product-type {
    margin-top: 30px;
    font-size: 40px;
    line-height: 1.12;
    color: var(--plum-deep);
  }
  .ingredient {
    margin-top: 30px;
    font-size: 15px;
    letter-spacing: 0.5px;
    color: var(--plum-deep);
  }
  .net-volume {
    margin-top: 30px;
    font-size: 17px;
    color: var(--plum-deep);
  }
</style>
</head>
<body>
  <article class="label">
    <div class="label__leaf-art" role="img" aria-label="Faint lime line-drawn leaf decoration sweeping across the label"></div>
    <div class="label__band label__band--top"></div>
    <div class="label__band label__band--bottom"></div>
    <div class="label__content">
      <div class="brand-mark"></div>
      <h1 class="brand-name">worrabee</h1>
      <p class="product-name">Silk</p>
      <p class="product-type">Lavender Scented<br>Lubricant</p>
      <p class="ingredient">100% MACADAMIA OIL</p>
      <p class="net-volume">8 oz 236.5ml</p>
    </div>
  </article>
</body>
</html>
```